Torvel, Inc. new buisness cards - brand guide included

We need new business cards. SLEAK SIMPLE FINANCE. They must include a place for NAME, TITLE, CELL, OFFICE PHONE, EMAIL. they also must include our services across the bottom. AIR, OCEAN, FTL, LTL, EXPRESS. for reference this will be being handed to some of the most prestigious shipping companies in a america.

Target Market(s)

Finance and corporate

Contact Information for Business Card

We need new business cards. SLEAK SIMPLE FINANCE. They must include a place for NAME, TITLE, CELL, OFFICE PHONE, EMAIL. they also must include our services across the bottom. AIR, OCEAN, FTL, LTL, EXPRESS.

Requirements
Must have
• We need new business cards. SLEAK SIMPLE FINANCE. They must include a place for NAME, TITLE, CELL, OFFICE PHONE, EMAIL. they also must include our services across the bottom. AIR, OCEAN, FTL, LTL, EXPRESS.
Nice to have
• USE THE COLORS AND LOGO IN THE BRAND GUIDE :)

```html
<!DOCTYPE html>
<html lang="en">
<head>
<meta charset="utf-8">
<title>Torvel, Inc. Business Card</title>
<link rel="stylesheet" href="https://fonts.googleapis.com/css2?family=Montserrat:wght@400;500;700&display=swap">
<style>
  :root {
    --backdrop: #161618;
    --card: #2d2d2f;
    --card-edge: #3a3a3c;
    --wordmark: #8a8a8d;
    --ink: #ececec;
    --muted: #cfcfcf;
    --gold: #c9b48e;
  }
  * { margin: 0; padding: 0; box-sizing: border-box; }
  html, body {
    width: 1200px; height: 947px; overflow: hidden;
    background: var(--backdrop);
    font-family: "Montserrat", sans-serif;
    color: var(--ink);
  }
  .sheet {
    width: 1200px; height: 947px;
    display: flex; flex-direction: column; align-items: center; justify-content: center;
    gap: 44px;
  }
  .card {
    position: relative;
    width: 700px; height: 400px;
    background: var(--card);
    border: 1px solid var(--card-edge);
    border-radius: 20px;
    overflow: hidden;
  }
  /* Front */
  .card--front { display: flex; flex-direction: column; align-items: center; justify-content: center; }
  .front__wordmark {
    font-size: 78px; font-weight: 500; letter-spacing: 10px;
    color: var(--wordmark); line-height: 1;
    margin-top: 10px;
  }
  .front__services {
    margin-top: 64px;
    font-size: 15px; font-weight: 400; letter-spacing: 1.6px;
    color: var(--ink);
  }
  .front__services .sep { margin: 0 10px; }
  /* Back */
  .back__wordmark {
    position: absolute; right: 40px; top: 40px;
    font-size: 40px; font-weight: 500; letter-spacing: 6px;
    color: var(--wordmark); line-height: 1;
  }
  .back__info { position: absolute; left: 60px; top: 96px; }
  .person__name {
    font-size: 30px; font-weight: 700; letter-spacing: 1px;
    color: var(--gold); line-height: 1.1;
  }
  .person__title { font-size: 16px; color: var(--muted); margin-top: 6px; }
  .divider { width: 10px; height: 2px; background: var(--gold); margin: 18px 0 12px; }
  .contact { list-style: none; }
  .contact li {
    display: flex; align-items: center; gap: 12px;
    font-size: 15px; line-height: 24px; color: var(--ink);
  }
  .contact svg { width: 14px; height: 14px; flex: none; }
  .contact__label { color: var(--gold); font-size: 13px; width: 14px; margin-right: -4px; }
  .address { font-size: 15px; line-height: 24px; color: var(--ink); }
</style>
</head>
<body>
<main class="sheet">

  <section class="card card--front" aria-label="Card front">
    <div class="front__wordmark">TORVEL</div>
    <p class="front__services">AIR<span class="sep">|</span>OCEAN<span class="sep">|</span>FTL<span class="sep">|</span>LTL<span class="sep">|</span>EXPRESS</p>
  </section>

  <section class="card card--back" aria-label="Card back">
    <div class="back__wordmark">TORVEL</div>
    <div class="back__info">
      <h1 class="person__name">EVERETT HALE</h1>
      <p class="person__title">CEO &amp; Founder</p>
      <div class="divider"></div>
      <ul class="contact">
        <li class="contact__cell">
          <svg viewBox="0 0 16 16" aria-label="Cell"><rect x="4" y="1" width="8" height="14" rx="1.5" fill="var(--gold)"/><rect x="5.5" y="3" width="5" height="8" fill="var(--card)"/><circle cx="8" cy="13" r="0.9" fill="var(--card)"/></svg>
          302-555-0148
        </li>
        <li class="contact__office">
          <svg viewBox="0 0 16 16" aria-label="Office"><path fill="var(--gold)" d="M4 1l2.5 3-1.6 1.6c.8 2 2.5 3.7 4.5 4.5L11 8.5 14 11l-1.5 3C7 13.5 2.5 9 2 3.5z"/></svg>
          302-555-0192
        </li>
        <li class="contact__email">
          <svg viewBox="0 0 16 16" aria-hidden="true"><rect x="1" y="3" width="14" height="10" rx="1" fill="var(--gold)"/><path d="M1.5 3.5L8 9l6.5-5.5" fill="none" stroke="var(--card)" stroke-width="1.3"/></svg>
          hello@torvelinc.com
        </li>
        <li class="contact__web">
          <svg viewBox="0 0 16 16" aria-hidden="true"><g fill="none" stroke="var(--gold)" stroke-width="1.3"><circle cx="8" cy="8" r="6.5"/><ellipse cx="8" cy="8" rx="3" ry="6.5"/><path d="M1.5 8h13"/></g></svg>
          www.torvelinc.com
        </li>
      </ul>
      <div class="divider"></div>
      <p class="address">2210 Harbor Line Rd Ste 110<br>Bellmont, WA 98000</p>
    </div>
  </section>

</main>
</body>
</html>
```